Zielgruppe
wir sind ein ambulanter Pflegedienst
Aufgabenstellung
Es soll ein Flyer entworfen werden.
Im Vordergrund steht die Behandlungspflege. Patienten sollen darauf aufmerksam gemacht werden, dass wir Insulininjektionen übernehmen und Kompressionsstrümpfe anziehen, wenn der Hausarzt dafür eine Verordnung ausstellt.
Im Vordergrund steht die Insulininjektion und das an und ausziehen der Kompressionsstrümpfe.
Falls die Patienten es nicht mehr alleine schaffen, springt der Pflegedienst ein.
Wichtig ist, dass das Pflegegeld nicht gekürzt wird, da dies eine Leistung der Krankenkasse ist.
Daten des Pflegedienstes:
Pflegehaus Lindental
Birkenweg 27
18057 Rostock
Tel 0800 4417236
www.Pflegehaus-Lindental.de
info@Pflegehaus-Lindental.de

```html
<!DOCTYPE html>
<html lang="de">
<head>
<meta charset="utf-8">
<title>Pflegehaus Lindental – Flyer Behandlungspflege</title>
<link rel="stylesheet" href="https://fonts.googleapis.com/css2?family=Montserrat:wght@800;900&family=Open+Sans:ital,wght@1,300;1,700;1,800&family=PT+Sans:wght@400&display=swap">
<style>
  :root {
    --orange: #ff7f2a;
    --blue: #0a4fe4;
    --green: #6cff2e;
    --white: #ffffff;
    --ink: #111111;
    --photo-light: #e4e4e8;
    --photo-skin: #d9a58f;
    --photo-shadow: #9b8f88;
  }
  * { margin: 0; padding: 0; box-sizing: border-box; }
  html, body { width: 846px; height: 1200px; overflow: hidden; background: var(--white); }
  .flyer { position: relative; width: 846px; height: 1200px; overflow: hidden; }

  .photo {
    position: absolute; inset: 0;
    background:
      radial-gradient(ellipse 220px 260px at 700px 330px, var(--photo-skin) 0%, rgba(217,165,143,0) 75%),
      radial-gradient(ellipse 180px 200px at 150px 260px, #dcbcae 0%, rgba(220,188,174,0) 75%),
      radial-gradient(ellipse 160px 180px at 60px 1050px, #b48c7e 0%, rgba(180,140,126,0) 80%),
      linear-gradient(170deg, #cbc3b8 0%, var(--photo-light) 40%, #e9e9ee 70%, var(--photo-shadow) 100%);
  }
  .bubbles { position: absolute; inset: 0; }

  .frame { position: absolute; inset: 0; pointer-events: none; }

  .headline {
    position: absolute; left: 20px; color: var(--white);
    font-family: "Montserrat", sans-serif; white-space: nowrap;
    background: var(--orange);
    clip-path: polygon(0 0, 100% 0, calc(100% - 12px) 100%, 0 100%);
  }
  .headline--main {
    top: 40px; width: 785px; height: 71px;
    font-weight: 900; font-size: 53px; letter-spacing: -1.5px;
    line-height: 71px; padding-left: 6px;
  }
  .headline--sub {
    top: 121px; width: 808px; height: 51px;
    font-weight: 900; font-size: 33px; letter-spacing: -1.6px;
    line-height: 53px; padding-left: 5px;
  }

  .service-text {
    position: absolute; left: 42px; top: 349px;
    font-family: "Open Sans", sans-serif; font-style: italic; font-weight: 800;
    font-size: 33px; letter-spacing: -0.6px; color: var(--white);
  }
  .service-text span {
    display: block; height: 44px; line-height: 44px; margin-bottom: 4px;
    padding-left: 6px; background: var(--blue); white-space: nowrap;
    clip-path: polygon(0 0, 100% 0, calc(100% - 8px) 100%, 0 100%);
  }
  .service-text span:nth-child(1) { width: 773px; }
  .service-text span:nth-child(2) { width: 763px; }
  .service-text span:nth-child(3) { width: 418px; }

  .brand {
    position: absolute; left: 380px; top: 790px; width: 400px; text-align: center;
    font-family: "PT Sans", sans-serif; font-weight: 400; font-size: 40px;
    color: var(--blue); line-height: 1.1;
  }

  .contact {
    position: absolute; left: 54px; top: 822px;
    font-family: "PT Sans", sans-serif; font-size: 27px; color: var(--ink);
    list-style: none;
  }
  .contact li {
    height: 32px; line-height: 32px; margin-bottom: 3.6px;
    padding-left: 4px; background: var(--green); white-space: nowrap;
  }
  .contact li.short { width: 259px; }
  .contact li.long { width: 374px; }

  .hotline-band { position: absolute; left: 0; top: 1070px; }
  .hotline {
    position: absolute; left: 22px; top: 1130px; display: flex; align-items: center;
    color: var(--white);
  }
  .hotline__icon { width: 48px; height: 48px; margin-right: 16px; }
  .hotline__number {
    font-family: "Montserrat", sans-serif; font-weight: 900; font-size: 57px;
    letter-spacing: -1px; line-height: 1;
  }
  .hotline__note {
    font-family: "Open Sans", sans-serif; font-style: italic; font-weight: 300;
    font-size: 40px; margin-left: 6px; line-height: 1;
  }
</style>
</head>
<body>
<main class="flyer">
  <div class="photo" role="img" aria-label="Unscharfes Foto: Pflegekraft im weißen Kittel betreut eine ältere Patientin"></div>

  <svg class="bubbles" width="846" height="1200" viewBox="0 0 846 1200" aria-hidden="true">
    <defs>
      <filter id="soft-shadow" x="-20%" y="-20%" width="140%" height="140%">
        <feDropShadow dx="0" dy="2" stdDeviation="4" flood-color="#000" flood-opacity="0.18"/>
      </filter>
    </defs>
    <circle cx="160" cy="210" r="180" fill="#ffffff" fill-opacity="0.22" filter="url(#soft-shadow)"/>
    <circle cx="90" cy="960" r="150" fill="#ffffff" fill-opacity="0.2" filter="url(#soft-shadow)"/>
    <circle cx="660" cy="790" r="300" fill="#f6f6f8" fill-opacity="0.82" filter="url(#soft-shadow)"/>
  </svg>

  <svg class="frame" width="846" height="1200" viewBox="0 0 846 1200" aria-hidden="true">
    <g stroke="#0a4fe4" stroke-width="5" stroke-dasharray="14 9" fill="none">
      <line x1="0" y1="3" x2="846" y2="3"/>
      <line x1="6" y1="0" x2="6" y2="1080"/>
      <line x1="840" y1="0" x2="840" y2="1080"/>
    </g>
  </svg>

  <h1 class="headline headline--main">WIR KÜMMERN UNS UM SIE !</h1>
  <h2 class="headline headline--sub">OHNE DASS IHR PFLEGEGELD GEKÜRZT WIRD !</h2>

  <p class="service-text">
    <span>Sowohl bei Insulininjektionen,als auch beim</span>
    <span>anziehen von Kompressionsstrümpfen sind</span>
    <span>wir jederzeit für Sie da !</span>
  </p>

  <div class="brand">Pflegehaus Lindental</div>

  <ul class="contact">
    <li class="short">Pflegehaus Lindental</li>
    <li class="short">Birkenweg 27</li>
    <li class="short">18057 Rostock</li>
    <li class="short">Tel.: 0800 4417236</li>
    <li class="long">www.Pflegehaus-Lindental.de</li>
    <li class="long">info@Pflegehaus-Lindental.de</li>
  </ul>

  <svg class="hotline-band" width="846" height="130" viewBox="0 1070 846 130" aria-hidden="true">
    <path d="M0 1080 Q423 1150 846 1078 L846 1200 L0 1200 Z" fill="#0a4fe4"/>
  </svg>

  <div class="hotline">
    <svg class="hotline__icon" viewBox="0 0 48 48" aria-hidden="true">
      <circle cx="24" cy="24" r="21" fill="none" stroke="#ffffff" stroke-width="4"/>
      <path d="M16 12c2 0 3 4 4 6 .5 1.2-1.5 2.5-1.5 3.5 1 3 4 6.5 7.5 8 1 0 2.2-2 3.5-1.6 2 .8 6 2 6 4 0 2.5-3 4.5-5 4.5-8.5-.5-17-9-17.5-17.5 0-2 1.5-6.9 3-6.9z" fill="#ffffff"/>
    </svg>
    <span class="hotline__number">0800 44172 36</span>
    <span class="hotline__note">(kostenlos)</span>
  </div>
</main>
</body>
</html>
```